GLS biz card

We need a business card design for our new company based in Los Angeles called "Gold Lantern Studios". We develop film and television projects. We work with investors, financiers, film production companies, film distribution and sales companies as well as studios. We would like to incorporate our logo (see attached) on a two-sided card. We need to include: name and title, address, phone, email and company website.

Target Market(s)

Business, financial and studio clients

Industry/Entity Type

Business

Contact Information for Business Card

Two-sided. We are thinking of the logo on one side and the information on the back. Please feel free to be creative! Thanks.

Requirements
Must have
• Please include the following text information, excluding the "CAPS CATEGORY:" and please allow the ability for us to change the name, title and email address for each company employee):
• NAME & TITLE:
• Peter Harlow
• Managing Partner
• COMPANY NAME:
• GOLD LANTERN STUDIOS (please use existing logo)
• COMPANY ADDRESS:
• TKV Media Campus
• 2840 Welwood Avenue
• Tarlow Center, 4th Floor
• Manhattan Beach, CA 90271
• COMPANY PHONE NUMBER:
• 310-555-0148
• COMPANY WEBSITE ADDRESS:
• www.goldlanternstudiosgroup.example
• EMAIL ADDRESS: (only one per card)
• martin@goldlanternstudiosgroup.example
• buzzy@goldlanternstudiosgroup.example
• peter@goldlanternstudiosgroup.example

```html
<!DOCTYPE html>
<html lang="en">
<head>
<meta charset="utf-8">
<title>Gold Lantern Studios – Business Card</title>
<link rel="stylesheet" href="https://fonts.googleapis.com/css2?family=Josefin+Sans:wght@400;600;700&display=swap">
<style>
  :root {
    --page-bg: #e9e9e9;
    --card-black: #000000;
    --accent: #29b6ea;
    --accent-light: #8fdcf7;
    --accent-deep: #0d7fb3;
    --text-white: #ffffff;
  }
  * { box-sizing: border-box; margin: 0; padding: 0; }
  html, body {
    width: 1200px; height: 1004px; overflow: hidden;
    background: var(--page-bg);
    font-family: "Josefin Sans", "Futura", sans-serif;
  }
  .card {
    position: absolute;
    top: 107px;
    width: 443px; height: 758px;
    background: var(--card-black);
    color: var(--text-white);
    overflow: hidden;
  }
  .card--front { left: 121px; }
  .card--back { left: 644px; }

  /* film strip bands */
  .film-band {
    position: absolute; left: 0; width: 100%; height: 69px;
    background: linear-gradient(to bottom, var(--accent-light), var(--accent) 60%, var(--accent-deep));
  }
  .film-band--top { top: 0; }
  .film-band--bottom { bottom: 0; }
  .film-band .perforation {
    position: absolute; top: 20px; width: 29px; height: 36px;
    background: var(--card-black);
  }

  .brand-dot {
    position: absolute; border-radius: 50%;
    background: var(--accent);
  }
  .brand-name {
    position: absolute; left: 0; width: 100%; text-align: center;
    font-weight: 700; color: var(--accent); letter-spacing: 2px;
  }
  .brand-tagline {
    position: absolute; left: 0; width: 100%; text-align: center;
    font-weight: 600; color: var(--text-white); letter-spacing: 2.6px;
  }

  .card--front .brand-dot { left: 161px; top: 270px; width: 120px; height: 120px; }
  .card--front .brand-name { top: 446px; font-size: 29px; line-height: 33px; }
  .card--front .brand-tagline { top: 522px; font-size: 13px; }

  .card--back .brand-dot { left: 176px; top: 90px; width: 90px; height: 90px; }
  .card--back .brand-name { top: 222px; font-size: 23px; line-height: 26px; }
  .card--back .brand-tagline { top: 284px; font-size: 10.5px; }

  .person-name {
    position: absolute; top: 344px; width: 100%; text-align: center;
    font-size: 30px; font-weight: 600; letter-spacing: 2.5px; line-height: 34px;
  }
  .person-title {
    position: absolute; top: 381px; width: 100%; text-align: center;
    font-size: 18px; font-weight: 600; letter-spacing: 3px; color: var(--accent); line-height: 22px;
  }
  .divider {
    position: absolute; left: 26px; width: 390px;
    border-top: 1.5px dashed var(--accent);
  }
  .divider--upper { top: 427px; }
  .divider--lower { top: 560px; }

  .contact-list { position: absolute; left: 30px; top: 443px; list-style: none; }
  .contact-item {
    display: flex; align-items: center; height: 34px;
    font-weight: 600; letter-spacing: 0.3px; white-space: nowrap;
  }
  .contact-item svg { width: 19px; height: 19px; margin-right: 9px; flex: none; }
  .contact-item--phone { font-size: 19px; letter-spacing: 2.5px; }
  .contact-item--email, .contact-item--web { font-size: 13px; }

  .location-pin { position: absolute; left: 212px; top: 578px; width: 18px; height: 22px; }
  .address {
    position: absolute; top: 612px; width: 100%; text-align: center;
    font-style: normal; font-weight: 600; letter-spacing: 1.3px; line-height: 22px; font-size: 16px;
  }
  .address .campus { font-size: 21px; letter-spacing: 2.2px; line-height: 26px; display: block; }
</style>
</head>
<body>

<section class="card card--front" aria-label="Card front">
  <div class="film-band film-band--top">
    <span class="perforation" style="left:33px"></span>
    <span class="perforation" style="left:90px"></span>
    <span class="perforation" style="left:148px"></span>
    <span class="perforation" style="left:206px"></span>
    <span class="perforation" style="left:263px"></span>
    <span class="perforation" style="left:321px"></span>
    <span class="perforation" style="left:378px"></span>
  </div>
  <div class="brand-dot" aria-hidden="true"></div>
  <div class="brand-name">GOLD LANTERN<br>STUDIOS</div>
  <div class="brand-tagline">A MEDIA ENTERTAINMENT COMPANY</div>
  <div class="film-band film-band--bottom">
    <span class="perforation" style="left:33px"></span>
    <span class="perforation" style="left:90px"></span>
    <span class="perforation" style="left:148px"></span>
    <span class="perforation" style="left:206px"></span>
    <span class="perforation" style="left:263px"></span>
    <span class="perforation" style="left:321px"></span>
    <span class="perforation" style="left:378px"></span>
  </div>
</section>

<section class="card card--back" aria-label="Card back">
  <div class="brand-dot" aria-hidden="true"></div>
  <div class="brand-name">GOLD LANTERN<br>STUDIOS</div>
  <div class="brand-tagline">A MEDIA ENTERTAINMENT COMPANY</div>

  <h1 class="person-name">PETER HARLOW</h1>
  <p class="person-title">MANAGING PARTNER</p>

  <div class="divider divider--upper"></div>
  <ul class="contact-list">
    <li class="contact-item contact-item--phone">
      <svg viewBox="0 0 24 24" aria-hidden="true"><path fill="#29b6ea" d="M6.6 10.8a15.1 15.1 0 0 0 6.6 6.6l2.2-2.2c.3-.3.7-.4 1-.2 1.1.4 2.3.6 3.6.6.6 0 1 .4 1 1V20c0 .6-.4 1-1 1A17 17 0 0 1 3 4c0-.6.4-1 1-1h3.5c.6 0 1 .4 1 1 0 1.3.2 2.5.6 3.6.1.3 0 .7-.2 1z"/></svg>
      (310) 555 0148
    </li>
    <li class="contact-item contact-item--email">
      <svg viewBox="0 0 24 24" aria-hidden="true"><rect x="2.5" y="5" width="19" height="14" fill="none" stroke="#29b6ea" stroke-width="2"/><path d="M2.5 5l9.5 8 9.5-8" fill="none" stroke="#29b6ea" stroke-width="2"/></svg>
      PETER@GOLDLANTERNSTUDIOSGROUP.EXAMPLE
    </li>
    <li class="contact-item contact-item--web">
      <svg viewBox="0 0 24 24" aria-hidden="true"><circle cx="10" cy="10" r="6.5" fill="none" stroke="#29b6ea" stroke-width="2.6"/><path d="M15 15l6 6" stroke="#29b6ea" stroke-width="3" stroke-linecap="round"/></svg>
      GOLDLANTERNSTUDIOSGROUP.EXAMPLE
    </li>
  </ul>
  <div class="divider divider--lower"></div>

  <svg class="location-pin" viewBox="0 0 18 22" aria-hidden="true"><path fill="#29b6ea" d="M9 0a7 7 0 0 0-7 7c0 5.3 7 15 7 15s7-9.7 7-15a7 7 0 0 0-7-7zm0 10a3 3 0 1 1 0-6 3 3 0 0 1 0 6z"/></svg>
  <address class="address">
    <span class="campus">TKV MEDIA CAMPUS</span>
    2840 WELWOOD AVENUE<br>
    TARLOW CENTER, 4TH FLOOR<br>
    MANHATTAN BEACH, CA 90271
  </address>
</section>

</body>
</html>
```